Business Card template designs

We need a lot of Business card designs.
Your designs will get exposure on our newly opened business-card printing website.
We are committed to quality of paper and packages we use, so they will come up very fancy.

Here is your advantage. We will put the profile of the graphic designer on our site so that you can showcase your designs to people around the world and in Japan.

A profile is not mandatory, although we encourage graphic designers to have a profile to get continuous work in the future.
We are looking forward to having many good designs.

The right of the use of design will be owned by us.
The design may be used to the products other than
business cards.

Target Market(s)

designer,photographer,creator,artist

Industry/Entity Type

Printing

Contact Information for Business Card

The back design is important.
Please check the reference file.

Requirements
Must have
• Please include the following, required information on your business card designs.
• Name: Haruna Okabe
• Title: Designer
• Web: https://www.ketori.co.jp/kt/
• Address: 4-17 Kamiharuta-Cho Meguro-ku, Tokyo
• Email: info@kketori.com
• Phone: 03 4816 3907
• Mobile: 070 2143 6658
• * For Japanese sites, we will convert the text portion to Japanese characters.
• * In case of 28mmx70mm only include Name,Enail,Phone and SNS account(https://www.facebook.com/kketori.com)
• 1. colorful
• 2. simple
• 3. natural
• 4. modern
• 5. cool
• 6. sporty
• Please make variations of the same image with 3-6
• different colors / patterns for one design so that
• customers can compare and choose.
• If you want to use a same picture, please make make
• copies and paste on each different types of design.
Nice to have
• You may also use, the following non-required information.
• Company Name: Ketori, Inc.
• Fax: 03-4173-9620
• Open space for company logo

```html
<!DOCTYPE html>
<html lang="en">
<head>
<meta charset="utf-8">
<title>Ketori Business Card</title>
<link rel="stylesheet" href="https://fonts.googleapis.com/css2?family=Mulish:ital,wght@0,400;0,600;0,700;1,400&display=swap">
<style>
  :root {
    --stage: #1e1e1f;
    --card-blue: #063089;
    --band-top: #0a2a78;
    --ink-light: #ffffff;
    --paper: #ffffff;
  }
  * { box-sizing: border-box; margin: 0; padding: 0; }
  html, body { width: 1200px; height: 987px; overflow: hidden; background: var(--stage); }
  body { position: relative; font-family: "Mulish", sans-serif; color: var(--ink-light); }

  .card {
    position: absolute;
    width: 615px;
    height: 351px;
    background: var(--card-blue);
    overflow: hidden;
  }
  .card--front { left: 293px; top: 131px; }
  .card--back  { left: 292px; top: 506px; }

  .brand-name {
    position: absolute;
    font-weight: 600;
    color: var(--ink-light);
    line-height: 1;
  }
  .card--front .brand-name {
    left: 0; right: 0; top: 42px;
    text-align: center;
    font-size: 64px;
    letter-spacing: 1px;
  }

  .name-row {
    position: absolute;
    left: 29px; right: 35px; top: 158px;
    display: flex; align-items: center; gap: 14px;
  }
  .name-row .rule { flex: 1; height: 1px; background: var(--ink-light); }
  .name-row .person { font-size: 21px; font-weight: 700; white-space: nowrap; }
  .name-row .role { font-size: 17px; font-weight: 400; }

  .company-block {
    position: absolute; left: 29px; top: 195px;
    font-size: 17px; line-height: 21.5px; font-style: normal;
  }
  .company-block .company { font-weight: 700; }

  .contact-list {
    position: absolute; right: 29px; top: 192px;
    list-style: none; font-size: 17px; line-height: 22.5px; text-align: right;
  }
  .contact-list li { display: flex; align-items: center; justify-content: flex-end; gap: 9px; }
  .contact-list svg { width: 16px; height: 16px; flex: none; }

  .footer-band {
    position: absolute; left: 0; right: 0; bottom: 0;
    height: 62px;
    background: linear-gradient(to bottom, var(--band-top) 0%, #5a7bc0 45%, var(--paper) 100%);
  }

  .card--back .brand-name {
    right: 31px; top: 222px;
    font-size: 62px; letter-spacing: 1px;
  }
  .back-url {
    position: absolute; right: 31px; top: 308px;
    font-size: 15px; font-style: italic; letter-spacing: 3.4px;
  }
</style>
</head>
<body>

<section class="card card--front" aria-label="Business card front">
  <div class="brand-name">Ketori</div>

  <div class="name-row">
    <span class="rule"></span>
    <span class="person">Haruna Okabe - <span class="role">Designer</span></span>
    <span class="rule"></span>
  </div>

  <address class="company-block">
    <div class="company">Ketori, Inc.</div>
    <div>4-17 Kamiharuta-Cho</div>
    <div>Meguro-ku, Tokyo</div>
    <div>www.ketori.com</div>
  </address>

  <ul class="contact-list">
    <li>03 4816 3907
      <svg viewBox="0 0 16 16" aria-hidden="true"><path fill="#fff" d="M3.5 1.5l2.5 0 1 3.5-1.7 1.3c.8 1.8 2.1 3.1 3.9 3.9l1.3-1.7 3.5 1v2.5c0 .8-.7 1.5-1.5 1.5C7 13.5 2 8.5 2 3 2 2.2 2.7 1.5 3.5 1.5z"/></svg>
    </li>
    <li>070 2143 6658
      <svg viewBox="0 0 16 16" aria-hidden="true"><rect x="4" y="1" width="8" height="14" rx="1.5" fill="none" stroke="#fff" stroke-width="1.6"/><rect x="7" y="12.2" width="2" height="1.2" fill="#fff"/></svg>
    </li>
    <li>03-4173-9620
      <svg viewBox="0 0 16 16" aria-hidden="true"><rect x="4" y="1.5" width="8" height="4" fill="#fff"/><rect x="1" y="6" width="14" height="6" rx="1" fill="#fff"/><rect x="4" y="10" width="8" height="4.5" fill="#fff" stroke="#063089" stroke-width="1"/></svg>
    </li>
    <li>info@kketori.com
      <svg viewBox="0 0 16 16" aria-hidden="true"><rect x="1" y="3.5" width="14" height="9.5" fill="#fff"/><path d="M1.5 4l6.5 5 6.5-5" fill="none" stroke="#063089" stroke-width="1.2"/></svg>
    </li>
  </ul>

  <div class="footer-band" role="img" aria-label="Decorative multicolour wave stripe along the bottom edge"></div>
</section>

<section class="card card--back" aria-label="Business card back">
  <div class="brand-name">Ketori</div>
  <div class="back-url">www.ketori.co.jp/kt</div>
</section>

</body>
</html>
```